A5 Certificate for a running Bluecrest Challenge

I would like a certificate designed called the "Bluecrest 50K Running Challenge"

It is presented to people that have run 50k in Mallorca across 10 runs. So they have to run 10 runs with a minimum distance of 5K per run. This gives a total of 50k.

The certificate will need:

1. Map of Mallorca in the background
2. Picture of a runner
3. Main title at the front to say "Bluecrest 50k Running Challenge"
4. Space to put the runners name on it. "Awarded to:"
5. Space to put the date the certificate is awarded. "Date Awarded:"

The design is then up to you but it needs to look official and professional. It is designed for teenagers so it needs to be "cool" and bold.

Any questions please ask.

Target Market(s)

Teenagers who want something cool and bold.

Font styles to use
Sans Serif

Colors
0556a4
fbee3f
33a6d7

Requirements
Must have
• 1. Map of Mallorca in the background
• 2. Picture of a runner
• 3. Main title at the front to say "Bluecrest 50k Running Challenge"
• 4. Space to put the runners name on it. "Awarded to:"
• 5. Space to put the date the certificate is awarded. "Date Awarded:"
Nice to have
• Mallorca is a sunny holiday location so it would be good to have sea blue colours and the sun in the design. to show the running challenge was done on a holiday island.

```html
<!DOCTYPE html>
<html lang="en">
<head>
<meta charset="utf-8">
<title>Bluecrest 50K Running Challenge – Certificate</title>
<link rel="stylesheet" href="https://fonts.googleapis.com/css2?family=Jost:wght@400;700&family=Source+Sans+3:wght@400&display=swap">
<style>
  :root {
    --page-bg: #e0e0e0;
    --paper: #ffffff;
    --title-blue: #1477c0;
    --line-blue: #1a86d6;
    --sea-top: #1d86cb;
    --sea-deep: #0e48a0;
    --sun-core: #f7e82c;
    --sun-edge: #e0a427;
    --runner-shade: #4d4413;
    --pattern-tint: #d6e8f5;
    --frame: #ffffff;
  }
  html, body {
    margin: 0;
    width: 1200px;
    height: 967px;
    overflow: hidden;
    background: var(--page-bg);
  }
  .certificate {
    position: absolute;
    left: 0;
    top: 57px;
    width: 1200px;
    height: 853px;
    background: var(--paper);
    overflow: hidden;
  }
  .line-texture {
    position: absolute;
    left: 0; top: 0;
    width: 1200px; height: 700px;
    background: radial-gradient(ellipse 75% 85% at 20% 45%, var(--pattern-tint) 0%, rgba(214,232,245,0.45) 45%, rgba(255,255,255,0) 75%);
  }
  .waves {
    position: absolute;
    left: 0; top: 0;
  }
  .title {
    position: absolute;
    left: 0; width: 1200px;
    margin: 0;
    text-align: center;
    font-family: "Jost", sans-serif;
    color: var(--title-blue);
    line-height: 1;
    text-transform: uppercase;
  }
  .title-main {
    top: 40px;
    left: 3px;
    font-weight: 700;
    font-size: 100px;
    letter-spacing: 2px;
  }
  .title-sub {
    top: 124px;
    left: 4px;
    font-weight: 400;
    font-size: 78px;
    letter-spacing: -0.5px;
  }
  .island-map {
    position: absolute;
    left: 348px; top: 210px;
    width: 482px; height: 345px;
    border-radius: 44% 40% 46% 50% / 40% 38% 62% 54%;
    background: radial-gradient(circle at 48% 45%, var(--sun-core) 0%, #ecc52a 45%, var(--sun-edge) 100%);
  }
  .runner {
    position: absolute;
    left: 543px; top: 250px;
    width: 129px; height: 228px;
    border-radius: 40% 40% 30% 30% / 22% 22% 18% 18%;
    background: var(--runner-shade);
  }
  .field-label {
    position: absolute;
    left: 0; width: 1200px;
    margin: 0;
    text-align: center;
    font-family: "Source Sans 3", sans-serif;
    font-weight: 400;
    text-transform: uppercase;
    line-height: 1;
  }
  .awarded-label {
    top: 557px;
    left: 22px;
    font-size: 32px;
    color: var(--line-blue);
  }
  .name-line {
    position: absolute;
    left: 323px; top: 630px;
    width: 577px; height: 4px;
    background: var(--line-blue);
  }
  .date-line {
    position: absolute;
    left: 515px; top: 786px;
    width: 165px; height: 1px;
    background: var(--frame);
  }
  .date-label {
    top: 794px;
    left: 1px;
    font-size: 26px;
    color: var(--frame);
  }
  .inner-frame {
    position: absolute;
    left: 24px; top: 18px;
    width: 1150px; height: 815px;
    border: 1px solid var(--frame);
    box-sizing: border-box;
  }
</style>
</head>
<body>
  <main class="certificate">
    <div class="line-texture" role="img" aria-label="Fine flowing blue line pattern sweeping across the background"></div>

    <svg class="waves" width="1200" height="853" viewBox="0 0 1200 853" aria-hidden="true">
      <defs>
        <linearGradient id="sea" x1="0" y1="0" x2="0" y2="1">
          <stop offset="0" stop-color="var(--sea-top)"/>
          <stop offset="0.5" stop-color="#1b8cd0"/>
          <stop offset="0.85" stop-color="var(--sea-deep)"/>
        </linearGradient>
        <radialGradient id="sun" cx="0.55" cy="0.75" r="0.6">
          <stop offset="0" stop-color="var(--sun-core)"/>
          <stop offset="0.5" stop-color="#eccb2a"/>
          <stop offset="1" stop-color="var(--sun-edge)"/>
        </radialGradient>
      </defs>
      <path class="sea-wave" fill="url(#sea)"
            d="M0,539 C300,660 620,695 900,652 L900,853 L0,853 Z"/>
      <path class="sun-wave" fill="url(#sun)"
            d="M1200,474 C1040,590 720,735 320,758 Q140,764 0,754 L0,853 L1200,853 Z"/>
    </svg>

    <div class="inner-frame"></div>

    <h1 class="title title-main">Bluecrest 50K</h1>
    <h2 class="title title-sub">Running Challenge</h2>

    <div class="island-map" role="img" aria-label="Golden map of Mallorca with a sunlit glow at its centre"></div>
    <div class="runner" role="img" aria-label="Dark silhouette of a runner in full stride"></div>

    <p class="field-label awarded-label">Awarded to</p>
    <div class="name-line"></div>

    <div class="date-line"></div>
    <p class="field-label date-label">Date awarded</p>
  </main>
</body>
</html>
```